K. Morendi needs an original business card for property investment professionals

The business card would be to present me as an investor in the real estate business. The market are developers of real estate projects, or other people who would like to sell and also to give us a name as a company. For style, colour and imagery I would like something artistic from Morendi (the artist) with a different touch.

Address, email, cel phone,
Updates

Hi¡ Update¡ I;d like it to stop providing Bright Acre as a Design and focus in K.Morendi.

Target Market(s)

Real Estate Developer/Investor

Industry/Entity Type

Real Estate

Colors
33a6d7
886aae
e3daeb
cadf82
f78f20

```html
<!DOCTYPE html>
<html lang="en">
<head>
<meta charset="utf-8">
<title>K.Morendi – Business Card</title>
<link rel="stylesheet" href="https://fonts.googleapis.com/css2?family=PT+Serif:wght@700&family=Arimo:wght@400&display=swap">
<style>
  :root {
    --card-bg: #fdfdfd;
    --ink: #0d0d0d;
    --band-red: #e8483d;
    --band-rose: #f0b3a6;
    --band-cream: #efe3dc;
    --band-blue: #6b73cc;
    --band-blue-deep: #4f58b8;
  }
  html, body {
    margin: 0;
    padding: 0;
    width: 1200px;
    height: 720px;
    overflow: hidden;
    background: var(--card-bg);
  }
  .card {
    position: relative;
    width: 1200px;
    height: 720px;
    background: var(--card-bg);
    overflow: hidden;
  }
  .card__art {
    position: absolute;
    inset: 0;
    width: 1200px;
    height: 720px;
  }
  .brand-name {
    position: absolute;
    left: 87px;
    top: 72px;
    margin: 0;
    font-family: "PT Serif", Georgia, serif;
    font-weight: 700;
    font-size: 84px;
    line-height: 1;
    letter-spacing: 0;
    color: var(--ink);
    text-transform: uppercase;
  }
  .holder {
    position: absolute;
    left: 631px;
    top: 312px;
    width: 489px;
  }
  .holder__name {
    margin: 0;
    font-family: "PT Serif", Georgia, serif;
    font-weight: 700;
    font-size: 78px;
    line-height: 1;
    letter-spacing: 2px;
    color: var(--ink);
  }
  .holder__rule {
    margin-top: 14px;
    height: 6px;
    background: var(--ink);
  }
  .contact {
    position: absolute;
    right: 83px;
    top: 492px;
    margin: 0;
    font-family: "Arimo", Arial, sans-serif;
    font-weight: 400;
    font-size: 38px;
    line-height: 48px;
    letter-spacing: 1px;
    color: var(--ink);
    text-align: right;
    font-style: normal;
  }
  .contact__line {
    display: block;
  }
</style>
</head>
<body>
  <main class="card">
    <svg class="card__art" viewBox="0 0 1200 720" role="img" aria-label="Diagonal band of faceted cubist-style artwork in red and blue tones">
      <defs>
        <linearGradient id="band-fill" x1="0" y1="0" x2="1" y2="0.35">
          <stop offset="0" stop-color="var(--band-red)"/>
          <stop offset="0.3" stop-color="var(--band-rose)"/>
          <stop offset="0.5" stop-color="var(--band-red)"/>
          <stop offset="0.6" stop-color="var(--band-cream)"/>
          <stop offset="0.66" stop-color="var(--band-blue)"/>
          <stop offset="1" stop-color="var(--band-blue-deep)"/>
        </linearGradient>
      </defs>
      <polygon class="art-band" points="0,158 729,720 373,720 0,432" fill="url(#band-fill)"/>
    </svg>

    <h1 class="brand-name">K.Morendi</h1>

    <section class="holder">
      <h2 class="holder__name">John Doe</h2>
      <div class="holder__rule"></div>
    </section>

    <address class="contact">
      <span class="contact__line">adress:48 Vale Street</span>
      <span class="contact__line">phone:555 318 274</span>
      <span class="contact__line">e-mail: info@k.morendi.com</span>
    </address>
  </main>
</body>
</html>
```